Comprehensive PWRPT

You helped develop our design recently and now I am looking for consistent branding around the 4 themes within our Company. The themes are all listed on Slide 1. I would like to create a powerpoint that summarizes the content for each theme using the color pallet and the content provided. Here are some bullets on the deliverable.:

• Each section of the pwrpt be in the color and the then listed either by heading or by slide layout
• Would like the 4 themes to be hyperlinked to each section allowing me to go wherever the presentation needs me to land. Also at the conclusion of each section, you can go back to the main page.
• All the content needed for each section is broken out and can be re-organized within that section, feel free to use different graphics I wanted to ensure I had the content needed.
• I am really looking for a master slide presentation of each of our 4 models but one that allows flexibility as you tell the story.

Any questions please let me know

```html
<!DOCTYPE html>
<html lang="en">
<head>
<meta charset="utf-8">
<title>Career Themes – Section Slides</title>
<link href="https://fonts.googleapis.com/css2?family=Poppins:ital,wght@0,600;0,700;0,800;1,300&display=swap" rel="stylesheet">
<style>
  :root {
    --backdrop: #232936;
    --slide-bg: #ffffff;
    --ink: #2b2f3a;
    --ink-soft: #4a4f5c;
    --supported-a: #f3b245;
    --supported-b: #f8c752;
    --prepared-a: #2f6a78;
    --prepared-b: #3e93a6;
    --engaged-a: #4a86d4;
    --engaged-b: #8bb3e2;
    --wise-a: #e86d1a;
    --wise-b: #f29d52;
    --bullet-orange: #f0a04a;
    --bullet-teal: #3a8a9c;
    --bullet-blue: #4f8fd8;
  }
  * { box-sizing: border-box; margin: 0; padding: 0; }
  html, body {
    width: 1200px; height: 900px; overflow: hidden;
    background: var(--backdrop);
    font-family: "Poppins", sans-serif;
  }
  .deck { position: relative; width: 1200px; height: 900px; }
  .slide {
    position: absolute; width: 499px; height: 281px;
    background: var(--slide-bg);
    box-shadow: 0 22px 40px rgba(0,0,0,0.35);
    overflow: hidden;
  }
  .slide--supported { left: 79px; top: 137px; }
  .slide--prepared  { left: 622px; top: 137px; }
  .slide--engaged   { left: 79px; top: 482px; }
  .slide--wise      { left: 622px; top: 482px; }

  .slide__header {
    position: absolute; left: 0; top: 0; width: 474px; height: 45px;
    border-bottom-right-radius: 30px;
    display: flex; align-items: center; padding-left: 23px;
  }
  .slide__title {
    color: #fff; font-weight: 700; font-size: 20px; letter-spacing: 0.2px;
  }
  .slide--supported .slide__header { background: linear-gradient(90deg, var(--supported-a), var(--supported-b)); }
  .slide--prepared  .slide__header { background: linear-gradient(90deg, var(--prepared-a), var(--prepared-b)); }
  .slide--engaged   .slide__header { background: linear-gradient(90deg, var(--engaged-a), var(--engaged-b)); }
  .slide--wise      .slide__header { background: linear-gradient(90deg, var(--wise-a), var(--wise-b)); }

  .slide__summary {
    position: absolute; left: 23px; z-index: 2;
    font-style: italic; font-weight: 300; font-size: 9.4px; line-height: 11.3px;
    color: var(--ink-soft);
  }
  .slide__topics { position: absolute; left: 23px; list-style: none; z-index: 2; }
  .slide__topic {
    position: relative; padding-left: 14px;
    font-weight: 700; font-size: 9.2px; line-height: 11.3px; color: var(--ink);
    margin-bottom: 6.2px;
  }
  .slide__topic svg { position: absolute; left: 0; top: 2px; width: 7px; height: 7px; }

  .slide__art { position: absolute; border-radius: 4px; z-index: 1; }

  .slide--supported .slide__summary { top: 72px; width: 250px; }
  .slide--supported .slide__topics  { top: 119px; width: 190px; }
  .slide--supported .slide__art {
    left: 218px; top: 116px; width: 269px; height: 153px;
    background: linear-gradient(135deg, #fbe6d6, #f4b866 55%, #6c9be6);
  }

  .slide--prepared .slide__summary { top: 92px; width: 182px; }
  .slide--prepared .slide__topics  { top: 150px; width: 200px; }
  .slide--prepared .slide__art {
    left: 240px; top: 66px; width: 237px; height: 196px;
    background: linear-gradient(135deg, #dbe7ef, #fdf0cf 50%, #27418f);
  }

  .slide--engaged .slide__summary { top: 69px; width: 178px; }
  .slide--engaged .slide__topics  { top: 127px; width: 180px; }
  .slide--engaged .slide__art {
    left: 212px; top: 102px; width: 272px; height: 166px;
    background: linear-gradient(135deg, #e6eef9, #a9c4e8 50%, #f08f3a);
  }

  .slide--wise .slide__summary { top: 87px; width: 152px; }
  .slide--wise .slide__topics  { top: 156px; width: 160px; }
  .slide--wise .slide__art {
    left: 200px; top: 81px; width: 277px; height: 181px;
    background: linear-gradient(160deg, #ffffff 10%, #2d4c9c 45%, #f0a24c 80%);
  }
</style>
</head>
<body>
<main class="deck">

  <section class="slide slide--supported">
    <header class="slide__header"><h2 class="slide__title">CAREER SUPPORTED</h2></header>
    <p class="slide__summary">Students are supported by informed educational leadership and policymaking that result in effective career resources and learning opportunities</p>
    <ul class="slide__topics">
      <li class="slide__topic"><svg viewBox="0 0 8 8"><g fill="var(--bullet-orange)"><circle cx="4" cy="1.3" r="1.3"/><circle cx="4" cy="6.7" r="1.3"/><circle cx="1.3" cy="4" r="1.3"/><circle cx="6.7" cy="4" r="1.3"/></g></svg>PathLink Policy Tools</li>
      <li class="slide__topic"><svg viewBox="0 0 8 8"><g fill="var(--bullet-orange)"><circle cx="4" cy="1.3" r="1.3"/><circle cx="4" cy="6.7" r="1.3"/><circle cx="1.3" cy="4" r="1.3"/><circle cx="6.7" cy="4" r="1.3"/></g></svg>Keystone V Technical Support</li>
      <li class="slide__topic"><svg viewBox="0 0 8 8"><g fill="var(--bullet-orange)"><circle cx="4" cy="1.3" r="1.3"/><circle cx="4" cy="6.7" r="1.3"/><circle cx="1.3" cy="4" r="1.3"/><circle cx="6.7" cy="4" r="1.3"/></g></svg>Professional Development</li>
      <li class="slide__topic"><svg viewBox="0 0 8 8"><g fill="var(--bullet-orange)"><circle cx="4" cy="1.3" r="1.3"/><circle cx="4" cy="6.7" r="1.3"/><circle cx="1.3" cy="4" r="1.3"/><circle cx="6.7" cy="4" r="1.3"/></g></svg>Industry-Education Relationships</li>
    </ul>
    <div class="slide__art" role="img" aria-label="Illustration: people helping each other climb rising blocks beside a potted plant"></div>
  </section>

  <section class="slide slide--prepared">
    <header class="slide__header"><h2 class="slide__title">CAREER PREPARED</h2></header>
    <p class="slide__summary">Students have the necessary foundational, technical, and workplace skillsneeded to support success in a variety of careers</p>
    <ul class="slide__topics">
      <li class="slide__topic"><svg viewBox="0 0 8 8"><g fill="var(--bullet-teal)"><circle cx="4" cy="1.3" r="1.3"/><circle cx="4" cy="6.7" r="1.3"/><circle cx="1.3" cy="4" r="1.3"/><circle cx="6.7" cy="4" r="1.3"/></g></svg>Career- Focused Curricula</li>
      <li class="slide__topic"><svg viewBox="0 0 8 8"><g fill="var(--bullet-teal)"><circle cx="4" cy="1.3" r="1.3"/><circle cx="4" cy="6.7" r="1.3"/><circle cx="1.3" cy="4" r="1.3"/><circle cx="6.7" cy="4" r="1.3"/></g></svg>Math Assessment with Scalar Career Database ( Scalar Career Database)</li>
    </ul>
    <div class="slide__art" role="img" aria-label="Illustration: person carrying a large pencil next to a checklist clipboard"></div>
  </section>

  <section class="slide slide--engaged">
    <header class="slide__header"><h2 class="slide__title">CAREER ENGAGED</h2></header>
    <p class="slide__summary">Students are motivated and inspired to develop career skills and seek employment opportunities that meet both personal and community needs</p>
    <ul class="slide__topics">
      <li class="slide__topic"><svg viewBox="0 0 8 8"><g fill="var(--bullet-blue)"><circle cx="4" cy="1.3" r="1.3"/><circle cx="4" cy="6.7" r="1.3"/><circle cx="1.3" cy="4" r="1.3"/><circle cx="6.7" cy="4" r="1.3"/></g></svg>Career Awareness &amp; Exposure</li>
      <li class="slide__topic"><svg viewBox="0 0 8 8"><g fill="var(--bullet-blue)"><circle cx="4" cy="1.3" r="1.3"/><circle cx="4" cy="6.7" r="1.3"/><circle cx="1.3" cy="4" r="1.3"/><circle cx="6.7" cy="4" r="1.3"/></g></svg>Purposeful Learning Connected to Careers</li>
    </ul>
    <div class="slide__art" role="img" aria-label="Illustration: team of professionals with a telescope and a rising arrow"></div>
  </section>

  <section class="slide slide--wise">
    <header class="slide__header"><h2 class="slide__title">CAREER WISE</h2></header>
    <p class="slide__summary">Students have insight into personal values and interests, as well as the economic realities of the job market, that supports informed career decisions</p>
    <ul class="slide__topics">
      <li class="slide__topic"><svg viewBox="0 0 8 8"><g fill="var(--bullet-orange)"><circle cx="4" cy="1.3" r="1.3"/><circle cx="4" cy="6.7" r="1.3"/><circle cx="1.3" cy="4" r="1.3"/><circle cx="6.7" cy="4" r="1.3"/></g></svg>Careers Pathways</li>
      <li class="slide__topic"><svg viewBox="0 0 8 8"><g fill="var(--bullet-orange)"><circle cx="4" cy="1.3" r="1.3"/><circle cx="4" cy="6.7" r="1.3"/><circle cx="1.3" cy="4" r="1.3"/><circle cx="6.7" cy="4" r="1.3"/></g></svg>Career Exploration</li>
      <li class="slide__topic"><svg viewBox="0 0 8 8"><g fill="var(--bullet-orange)"><circle cx="4" cy="1.3" r="1.3"/><circle cx="4" cy="6.7" r="1.3"/><circle cx="1.3" cy="4" r="1.3"/><circle cx="6.7" cy="4" r="1.3"/></g></svg>Educator Career Guides</li>
    </ul>
    <div class="slide__art" role="img" aria-label="Illustration: businessman riding a paper plane toward a red flag"></div>
  </section>

</main>
</body>
</html>
```